Single Page Timetracking Dashboard Desktop App UI Design (Figma Link required)

Main Idea: a SaaS tool where employees can add their time and project in a playful way. There is a infographics and a list with tasks as well.

Based on the attached concept.png the brief is following:

- check the attached rough scribble
- add own ideas or change things if they add value
- Style: colourful, nerdy, professional saas, modern, beautiful, white space
- Quality expectation: inspiration1+2.png
- I will need a Figma link
- desktop only
- make something fresh and unique

Process:
I need to include 2-3 feedback rounds that will span probably around 7 days

Target Market(s)

Internal Business Tool for a Software Development Company

Industry/Entity Type

IT

Other font styles liked:
• Could be monospace, not a must though

Requirements
Must have
• At least one page; Figma Link to the design;
Nice to have
• Microinterations like drop-down, hover/active colors; functionality specifications
Should not have
• Mobile view

```html
<!DOCTYPE html>
<html lang="en">
<head>
<meta charset="utf-8">
<title>Time Tracking Dashboard</title>
<link href="https://fonts.googleapis.com/css2?family=Poppins:wght@400;500;600&family=Space+Mono:wght@400;700&display=swap" rel="stylesheet">
<style>
:root{
  --page:#f6f7f1;
  --panel:#ffffff;
  --ink:#1c1c28;
  --muted:#8a8a98;
  --line:#e7e7ee;
  --chip:#fdf4e1;
  --orange:#f5821f;
  --orange-a:#f26a22;
  --orange-b:#f4b43a;
  --red:#f0532d;
  --blue:#3d4fdc;
  --violet:#c84ff0;
  --side:#ffffff;
}
*{box-sizing:border-box;margin:0;padding:0}
html,body{width:1200px;height:2469px;overflow:hidden}
body{font-family:"Poppins",sans-serif;color:var(--ink);background:var(--page);display:flex}
.mono{font-family:"Space Mono",monospace}

.sidebar{width:150px;height:2469px;background:var(--side);position:relative;padding-top:62px}
.nav-item{display:flex;align-items:center;gap:10px;height:40px;padding-left:30px;font-family:"Space Mono",monospace;font-size:11px;color:var(--muted);margin-bottom:2px}
.nav-item.active{background:#f4f5fb;color:var(--blue);border-left:5px solid var(--blue);padding-left:25px}
.nav-item svg{width:16px;height:16px}
.logout{position:absolute;left:30px;bottom:150px;display:flex;align-items:center;gap:10px;font-family:"Space Mono",monospace;font-size:10px;color:var(--muted)}

.main{flex:1;padding:46px 60px 0 35px}
.section-title{display:flex;align-items:center;gap:10px;font-size:21px;font-weight:500;letter-spacing:.2px;text-transform:uppercase}
.badge{width:34px;height:34px;border-radius:50%;display:grid;place-items:center}
.badge.orange{background:linear-gradient(135deg,var(--orange-a),var(--orange-b))}
.badge.violet{background:linear-gradient(135deg,var(--blue),var(--violet))}

.track{margin-top:18px;background:var(--panel);border-radius:14px;padding:20px 22px 44px;height:370px}
.track-top{display:flex;gap:22px}
.calendar{width:205px;border:1px solid var(--line);border-radius:12px;padding:14px 14px 10px}
.cal-head{display:flex;justify-content:space-between;align-items:center;font-size:11px;font-weight:500;margin-bottom:16px}
.cal-arrow{width:14px;height:14px;border-radius:50%;background:#f1f1f4;font-size:8px;display:grid;place-items:center;color:var(--muted)}
.cal-grid{display:grid;grid-template-columns:repeat(7,1fr);row-gap:8px;text-align:center;font-size:8px}
.cal-grid .dow{font-size:5.5px;color:var(--muted)}
.cal-grid .dim{color:#b8b8c2}
.cal-grid .today{background:#4a34e0;color:#fff;border-radius:3px;width:18px;height:18px;line-height:18px;margin:-4px auto}

.pickers{width:205px;display:flex;flex-direction:column;gap:10px}
.select{height:28px;border-radius:14px;background:#f7f7fa;font-size:9px;font-weight:500;display:flex;align-items:center;justify-content:space-between;padding:0 14px}
.recent{margin-top:4px;height:118px;border-radius:10px;background:linear-gradient(135deg,var(--blue),var(--violet));padding:14px 16px;color:#fff;font-size:8px}
.recent .row{display:flex;padding:5px 0;border-bottom:1px solid rgba(255,255,255,.35)}
.recent .row:last-child{border:none}
.recent .who{width:62px}

.chips{flex:1;display:grid;grid-template-columns:repeat(4,1fr);column-gap:14px}
.chip{height:44px;border-radius:6px;background:var(--chip);display:grid;place-items:center;font-family:"Space Mono",monospace;font-size:10px}
.chip.on{background:linear-gradient(100deg,var(--orange-a),var(--orange-b));color:#fff;box-shadow:0 8px 14px rgba(242,106,34,.3)}
.chips .r1{margin-bottom:12px}
.and{grid-column:1/5;text-align:center;font-size:8px;font-weight:500;height:30px;line-height:30px}

.track-bottom{display:flex;gap:14px;margin-top:28px}
.note{width:430px;height:70px;border-radius:12px;background:#f8f9fb;padding:14px 20px;font-size:9px;font-weight:500;display:flex;gap:6px}
.total{flex:1;height:70px;border-radius:14px;background:#fdf8ec;display:flex;align-items:center;padding:0 12px;gap:14px}
.total-time{flex:1;height:50px;border-radius:25px;background:#fff;display:flex;align-items:center;gap:16px;padding-left:40px;color:var(--orange);font-size:27px;font-weight:500}
.save{width:136px;height:50px;border-radius:25px;background:linear-gradient(100deg,var(--blue),var(--violet));color:#fff;font-size:12px;font-weight:600;display:grid;place-items:center}

.stat-head{margin-top:56px;display:flex;justify-content:space-between;align-items:center}
.period{height:28px;width:108px;border:1px solid var(--line);border-radius:14px;background:#fff;font-size:9px;font-weight:500;display:flex;align-items:center;justify-content:space-between;padding:0 14px 0 22px}
.stat-cards{display:flex;gap:34px;margin-top:24px}
.stat{flex:1;height:200px;background:#fff;border-radius:12px;padding:18px 20px;box-shadow:0 6px 24px rgba(40,40,80,.05)}
.stat-top{display:flex;justify-content:space-between;font-size:12px}
.stat-top .sum{color:var(--red);font-size:11px;font-weight:500}
.stat-body{display:flex;align-items:center;gap:24px;margin-top:10px}
.legend{flex:1;font-size:11px}
.legend .li{display:flex;align-items:center;height:23px}
.legend .h{width:56px}
.legend .c{width:80px}
.bar{flex:1;height:4px;border-radius:2px;background:#eeeef2;margin:0 10px 0 0;position:relative}
.bar i{position:absolute;left:0;top:0;bottom:0;border-radius:2px;background:linear-gradient(90deg,var(--red),#f7825f)}
.legend .p{width:30px;text-align:right}

.view-all{text-align:center;font-size:12px;color:var(--blue);margin-top:40px;display:flex;justify-content:center;align-items:center;gap:8px}
.page-no{text-align:center;font-size:7px;color:var(--muted);margin-top:22px}

.task-head{display:flex;justify-content:space-between;align-items:center;margin-top:8px}
.filter{width:104px;height:28px;border-radius:14px;background:#fff;font-size:9px;display:flex;align-items:center;justify-content:center;gap:6px}
.day{display:flex;justify-content:space-between;align-items:center;font-size:18px;font-weight:500;text-transform:uppercase;margin:44px 0 14px 6px}
.day .label{display:flex;align-items:center;gap:10px}
.task{background:#fff;border-radius:12px;overflow:hidden;box-shadow:0 6px 24px rgba(40,40,80,.05);margin:0 0 26px 6px}
.task-bar{height:62px;background:linear-gradient(90deg,var(--blue),var(--violet));display:flex;align-items:center;justify-content:space-between;padding:0 28px 0 45px;color:#fff;font-size:21px;font-weight:500}
.task-bar .tools{display:flex;gap:20px}
.task-body{display:flex;padding:22px 24px 34px 40px;height:126px}
.task-info{flex:1;padding-right:40px;border-right:1px solid var(--line)}
.task-meta{font-size:14px;font-weight:600;display:flex;gap:28px}
.task-text{font-size:11.5px;color:var(--muted);line-height:1.6;margin-top:12px}
.task-time{width:150px;text-align:center;padding-top:12px}
.task-time .d{color:var(--orange);font-size:21px;font-weight:500;line-height:1.1}
.task-time .w{font-size:14px}
.show-all{text-align:center;font-size:12px;color:var(--blue);margin-top:40px;display:flex;justify-content:center;align-items:center;gap:12px}
</style>
</head>
<body>
<aside class="sidebar">
  <div class="nav-item active"><svg viewBox="0 0 16 16"><circle cx="8" cy="8" r="8" fill="#6a4de6"/><path d="M8 4v4l3 2" stroke="#fff" stroke-width="1.5" fill="none"/></svg>Time</div>
  <div class="nav-item"><svg viewBox="0 0 16 16"><path d="M7 1a7 7 0 1 0 8 8H7z" fill="#9a9aa8"/><path d="M9 0v7h7a7 7 0 0 0-7-7z" fill="#c3c3cc"/></svg>Statistic</div>
  <div class="nav-item"><svg viewBox="0 0 16 16"><rect x="1" y="2" width="14" height="12" rx="3" fill="#a5a5b2"/><path d="M4 6h8M4 10h6" stroke="#fff" stroke-width="1.4"/></svg>Task</div>
  <div class="nav-item"><svg viewBox="0 0 16 16"><circle cx="8" cy="4.5" r="3.5" fill="#a5a5b2"/><path d="M1 15a7 5 0 0 1 14 0z" fill="#a5a5b2"/></svg>Account</div>
  <div class="logout"><svg width="22" height="20" viewBox="0 0 22 20" fill="none" stroke="#8a8a98" stroke-width="1.5"><path d="M9 2H2v16h7"/><path d="M20 10H7M11 6l-4 4 4 4"/></svg>Logout</div>
</aside>

<main class="main">
  <h1 class="section-title"><span class="badge orange"><svg width="18" height="18" viewBox="0 0 18 18" fill="none" stroke="#fff" stroke-width="1.6"><circle cx="9" cy="9" r="7"/><path d="M9 5v4l3 2"/></svg></span>Track your time</h1>

  <section class="track">
    <div class="track-top">
      <div class="calendar">
        <div class="cal-head"><span class="cal-arrow">‹</span>July 2023<span class="cal-arrow">›</span></div>
        <div class="cal-grid">
          <span class="dow">SUN</span><span class="dow">MON</span><span class="dow">TUE</span><span class="dow">WED</span><span class="dow">THU</span><span class="dow">FRI</span><span class="dow">SAT</span>
          <span class="dim">30</span><span class="dim">31</span><span>1</span><span>2</span><span>3</span><span>4</span><span>5</span>
          <span>6</span><span>7</span><span>8</span><span>9</span><span class="today">10</span><span>11</span><span>12</span>
          <span>13</span><span>14</span><span>15</span><span>16</span><span>17</span><span>18</span><span>19</span>
          <span>20</span><span>21</span><span>22</span><span>23</span><span>24</span><span>25</span><span>26</span>
          <span>27</span><span>28</span><span>29</span><span>30</span><span class="dim">1</span><span class="dim">2</span><span class="dim">3</span>
        </div>
      </div>
      <div class="pickers">
        <div class="select">Select project<svg width="9" height="6" viewBox="0 0 9 6" fill="none" stroke="#1c1c28" stroke-width="1.3"><path d="M1 1l3.5 3.5L8 1"/></svg></div>
        <div class="select">Select type<svg width="9" height="6" viewBox="0 0 9 6" fill="none" stroke="#1c1c28" stroke-width="1.3"><path d="M1 1l3.5 3.5L8 1"/></svg></div>
        <div class="recent">
          <div class="row"><span class="who">Alex Rowe</span>Collecting Data</div>
          <div class="row"><span class="who">Mina KT</span>Call customer</div>
          <div class="row"><span class="who">Tomas</span>Collect administra..</div>
          <div class="row"><span class="who">Lena Vor...</span>Find supplier for...</div>
        </div>
      </div>
      <div class="chips">
        <div class="chip on r1">1h</div><div class="chip r1">2h</div><div class="chip r1">3h</div><div class="chip r1">4h</div>
        <div class="chip">5h</div><div class="chip">6h</div><div class="chip">7h</div><div class="chip">8h</div>
        <div class="and">AND</div>
        <div class="chip">0m</div><div class="chip on">15m</div><div class="chip">30m</div><div class="chip">45</div>
      </div>
    </div>
    <div class="track-bottom">
      <div class="note"><svg width="10" height="10" viewBox="0 0 10 10" fill="none" stroke="#1c1c28" stroke-width="1.1"><path d="M1 9l1-3 5-5 2 2-5 5zM1 9.5h8"/></svg>What did you do?</div>
      <div class="total">
        <div class="total-time"><svg width="26" height="26" viewBox="0 0 26 26" fill="none" stroke="#f5821f" stroke-width="2"><circle cx="13" cy="13" r="11" stroke-dasharray="3 3"/><path d="M13 7v6l4 3"/></svg>1h 15m</div>
        <div class="save">SAVE</div>
      </div>
    </div>
  </section>

  <div class="stat-head">
    <h2 class="section-title"><span class="badge violet"><svg width="18" height="18" viewBox="0 0 18 18"><path d="M8 2a7 7 0 1 0 8 8H8z" fill="#fff"/><path d="M10 0v8h8a8 8 0 0 0-8-8z" fill="#e7dcff"/></svg></span>Statistic</h2>
    <div class="period">Monate<svg width="9" height="6" viewBox="0 0 9 6" fill="none" stroke="#1c1c28" stroke-width="1.3"><path d="M1 1l3.5 3.5L8 1"/></svg></div>
  </div>

  <div class="stat-cards">
    <div class="stat">
      <div class="stat-top"><span>Current Month</span><span class="sum">Total: 50:5 h</span></div>
      <div class="stat-body">
        <svg width="136" height="136" viewBox="0 0 136 136" role="img" aria-label="Donut chart of hours per customer">
          <defs>
            <linearGradient id="gO" x1="0" y1="0" x2="0" y2="1"><stop offset="0" stop-color="#f7a030"/><stop offset="1" stop-color="#f04f2f"/></linearGradient>
            <linearGradient id="gV" x1="0" y1="0" x2="1" y2="0"><stop offset="0" stop-color="#9a46ee"/><stop offset="1" stop-color="#d24ff0"/></linearGradient>
          </defs>
          <g transform="rotate(-100 68 68)" fill="none" stroke-width="34">
            <circle cx="68" cy="68" r="50" stroke="url(#gV)" stroke-dasharray="95 400"/>
            <circle cx="68" cy="68" r="50" stroke="#3d4fdc" stroke-dasharray="0 97 70 400"/>
            <circle cx="68" cy="68" r="50" stroke="url(#gO)" stroke-dasharray="0 169 143 400"/>
          </g>
        </svg>
        <div class="legend" style="margin-top:46px">
          <div class="li"><span class="h">40:45 h</span><span class="c">Customer A</span><span class="bar"><i style="width:89%"></i></span><span class="p">89%</span></div>
          <div class="li"><span class="h">08:45 h</span><span class="c">Customer B</span><span class="bar"><i style="width:78%"></i></span><span class="p">78%</span></div>
        </div>
      </div>
    </div>
    <div class="stat">
      <div class="stat-top"><span>September</span><span class="sum">Gesamt: 114:00 h</span></div>
      <div class="stat-body" style="margin-top:4px">
        <svg width="136" height="136" viewBox="0 0 136 136" role="img" aria-label="Donut chart of monthly hours per customer">
          <defs>
            <linearGradient id="gO2" x1="0" y1="0" x2="1" y2="1"><stop offset="0" stop-color="#f04f2f"/><stop offset="1" stop-color="#f7a030"/></linearGradient>
            <linearGradient id="gV2" x1="0" y1="0" x2="1" y2="0"><stop offset="0" stop-color="#9a46ee"/><stop offset="1" stop-color="#d24ff0"/></linearGradient>
          </defs>
          <g transform="rotate(175 68 68)" fill="none" stroke-width="34">
            <circle cx="68" cy="68" r="50" stroke="url(#gV2)" stroke-dasharray="125 400"/>
            <circle cx="68" cy="68" r="50" stroke="#3d4fdc" stroke-dasharray="0 128 62 400"/>
            <circle cx="68" cy="68" r="50" stroke="url(#gO2)" stroke-dasharray="0 193 118 400"/>
          </g>
        </svg>
        <div class="legend">
          <div class="li"><span class="h">40:45 h</span><span class="c">Customer A</span><span class="bar"><i style="width:89%"></i></span><span class="p">89%</span></div>
          <div class="li"><span class="h">08:45 h</span><span class="c">Customer B</span><span class="bar"><i style="width:78%"></i></span><span class="p">78%</span></div>
          <div class="li"><span class="h">08:45 h</span><span class="c">Customer C</span><span class="bar"><i style="width:13%"></i></span><span class="p">13%</span></div>
          <div class="li"><span class="h">08:45 h</span><span class="c">Customer C</span><span class="bar"><i style="width:4%"></i></span><span class="p">2%</span></div>
          <div class="li"><span class="h">08:45 h</span><span class="c">Customer D</span><span class="bar"><i style="width:55%"></i></span><span class="p">55%</span></div>
        </div>
      </div>
    </div>
  </div>

  <div class="view-all">View all <svg width="14" height="12" viewBox="0 0 14 12" fill="none" stroke="#3d4fdc" stroke-width="1.4"><path d="M1 6h12M8 1l5 5-5 5"/></svg></div>
  <div class="page-no">25</div>

  <div class="task-head">
    <h2 class="section-title"><span class="badge orange"><svg width="16" height="16" viewBox="0 0 16 16"><rect x="1" y="2" width="14" height="12" rx="3" fill="#fff"/><path d="M4 6h8M4 10h6" stroke="#f5821f" stroke-width="1.4"/></svg></span>Your task</h2>
    <div class="filter"><svg width="12" height="10" viewBox="0 0 12 10" fill="none" stroke="#1c1c28" stroke-width="1.1"><path d="M0 2.5h12M0 7.5h12"/><circle cx="4" cy="2.5" r="1.6" fill="#fff"/><circle cx="8" cy="7.5" r="1.6" fill="#fff"/></svg>Filter</div>
  </div>

  <div class="day"><span class="label"><svg width="20" height="20" viewBox="0 0 20 20" fill="none" stroke="#1c1c28" stroke-width="1.5"><rect x="2" y="3" width="16" height="15" rx="2"/><path d="M6 1v4M14 1v4M5.5 10h1M9.5 10h1M13.5 10h1M5.5 14h1M9.5 14h1M13.5 14h1"/></svg>Wednesday</span><span>7H 30M</span></div>
  <article class="task">
    <div class="task-bar"><span>Coding</span><span class="tools"><svg width="18" height="18" viewBox="0 0 18 18" fill="none" stroke="#fff" stroke-width="1.4"><path d="M2 16l1-4 9-9 3 3-9 9zM2 17h14"/></svg><svg width="16" height="18" viewBox="0 0 16 18" fill="none" stroke="#fff" stroke-width="1.4"><path d="M1 4h14M5 4V1.5h6V4M3 4l1 13h8l1-13"/></svg></span></div>
    <div class="task-body"><div class="task-info"><div class="task-meta"><span>Customer A</span><span>Project 1</span></div><p class="task-text">Lorem ipsum dolor sit amet consectetur. Amet velit tristique non urna eget orci ornare pulvinar. Aliquet velit mollis morbi ut non vitae nulla. Praesent luctus porttitor sed sed congue molestie tempor. Non et pharetra vestibulum</p></div><div class="task-time"><div class="d">4h 30m</div><div class="w">December 9th</div></div></div>
  </article>

  <div class="day"><span class="label"><svg width="20" height="20" viewBox="0 0 20 20" fill="none" stroke="#1c1c28" stroke-width="1.5"><rect x="2" y="3" width="16" height="15" rx="2"/><path d="M6 1v4M14 1v4M5.5 10h1M9.5 10h1M13.5 10h1M5.5 14h1M9.5 14h1M13.5 14h1"/></svg>Thuesday</span></div>
  <article class="task">
    <div class="task-bar"><span>Project Management</span><span class="tools"><svg width="18" height="18" viewBox="0 0 18 18" fill="none" stroke="#fff" stroke-width="1.4"><path d="M2 16l1-4 9-9 3 3-9 9zM2 17h14"/></svg><svg width="16" height="18" viewBox="0 0 16 18" fill="none" stroke="#fff" stroke-width="1.4"><path d="M1 4h14M5 4V1.5h6V4M3 4l1 13h8l1-13"/></svg></span></div>
    <div class="task-body"><div class="task-info"><div class="task-meta"><span>Customer A</span><span>Project 1</span></div><p class="task-text">Lorem ipsum dolor sit amet consectetur. Amet velit tristique non urna eget orci ornare pulvinar. Aliquet velit mollis morbi ut non vitae nulla. Praesent luctus porttitor sed sed congue molestie tempor. Non et pharetra vestibulum</p></div><div class="task-time"><div class="d">4h 30m</div><div class="w">December 9th</div></div></div>
  </article>
  <article class="task">
    <div class="task-bar"><span>Meeting</span><span class="tools"><svg width="18" height="18" viewBox="0 0 18 18" fill="none" stroke="#fff" stroke-width="1.4"><path d="M2 16l1-4 9-9 3 3-9 9zM2 17h14"/></svg><svg width="16" height="18" viewBox="0 0 16 18" fill="none" stroke="#fff" stroke-width="1.4"><path d="M1 4h14M5 4V1.5h6V4M3 4l1 13h8l1-13"/></svg></span></div>
    <div class="task-body"><div class="task-info"><div class="task-meta"><span>Customer A</span><span>Project 1</span></div><p class="task-text">Lorem ipsum dolor sit amet consectetur. Amet velit tristique non urna eget orci ornare pulvinar. Aliquet velit mollis morbi ut non vitae nulla. Praesent luctus porttitor sed sed congue molestie tempor. Non et pharetra vestibulum</p></div><div class="task-time"><div class="d">4h 30m</div><div class="w">December 9th</div></div></div>
  </article>

  <div class="day"><span class="label"><svg width="20" height="20" viewBox="0 0 20 20" fill="none" stroke="#1c1c28" stroke-width="1.5"><rect x="2" y="3" width="16" height="15" rx="2"/><path d="M6 1v4M14 1v4M5.5 10h1M9.5 10h1M13.5 10h1M5.5 14h1M9.5 14h1M13.5 14h1"/></svg>Thuesday</span></div>
  <article class="task">
    <div class="task-bar"><span>Meeting</span><span class="tools"><svg width="18" height="18" viewBox="0 0 18 18" fill="none" stroke="#fff" stroke-width="1.4"><path d="M2 16l1-4 9-9 3 3-9 9zM2 17h14"/></svg><svg width="16" height="18" viewBox="0 0 16 18" fill="none" stroke="#fff" stroke-width="1.4"><path d="M1 4h14M5 4V1.5h6V4M3 4l1 13h8l1-13"/></svg></span></div>
    <div class="task-body"><div class="task-info"><div class="task-meta"><span>Customer A</span><span>Project 1</span></div><p class="task-text">Lorem ipsum dolor sit amet consectetur. Amet velit tristique non urna eget orci ornare pulvinar. Aliquet velit mollis morbi ut non vitae nulla. Praesent luctus porttitor sed sed congue molestie tempor. Non et pharetra vestibulum</p></div><div class="task-time"><div class="d">4h 30m</div><div class="w">December 9th</div></div></div>
  </article>

  <div class="show-all">SHow all <svg width="14" height="12" viewBox="0 0 14 12" fill="none" stroke="#3d4fdc" stroke-width="1.4"><path d="M1 6h12M8 1l5 5-5 5"/></svg></div>
</main>
</body>
</html>
```